2 Page Web Design Project (coded)

What does the company do?
Pilot contracting, flying private/corporate jets.

What is its target market?
The target market is primarily the private jet management market, i.e. companies, which specialize in private aircraft management and are looking to fill crew positions on a short/long term basis, usually on short notice basis

How many pages should your website include?
2 Pages: 1/ Front Page with Company Logo, 2/ Services and Contact page

Do you want coding included? YES

Do you have any style you would like your website to have?
The main colors of my logo should be kept. Please see attached business card logo.

Other Instructions: Please see Veltrane's website (media section) for Skyrunner 418 pictures for free download, which can be incorporated into the website. Link: http://www.veltrane-example.com/en/aerospace/media-centre/multimedia-library/details?categoryID=L3-Veltrane%20Skyrunner%20418%20Aircraft.

Please see www.skylinehandoverdesk-example.com for services description.
Find attached source file business card and use loge design/font for website, so both business card and website are consistent.

Industry/Entity Type

Business

Requirements
Must have
• email link to link to my personal email, without giving my email address.

```html
<!DOCTYPE html>
<html lang="en">
<head>
<meta charset="utf-8">
<title>Meridian Crew Leasing – Services</title>
<link rel="stylesheet" href="https://fonts.googleapis.com/css2?family=PT+Sans:wght@400;700&display=swap">
<style>
:root{
  --page-bg:#ebebed;
  --top-bar:#4a4a4b;
  --band:#d8d8da;
  --frame:#5f5f60;
  --brand:#3a2a1f;
  --ink:#1e1e1e;
  --rule:#9a9a9a;
  --panel-border:#cfcfd2;
  --nav-accent:#e2561b;
  --footer:#000;
  --footer-text:#d6d6d6;
}
*{margin:0;padding:0;box-sizing:border-box}
html,body{width:1200px;height:1083px;overflow:hidden}
body{position:relative;background:var(--page-bg);font-family:"PT Sans",sans-serif;color:var(--ink)}
.top-bar{position:absolute;left:0;top:0;width:1200px;height:14px;background:var(--top-bar)}
.brand{position:absolute;left:160px;top:32px;width:300px;text-align:center}
.brand-mark{width:34px;height:34px;border-radius:50%;background:var(--brand);margin:0 auto 14px}
.brand-name{font-size:30px;font-weight:400;letter-spacing:1.5px;color:var(--brand);text-transform:uppercase}
.hero-band{position:absolute;left:0;top:171px;width:1200px;height:292px;background:var(--band)}
.hero-frame{position:absolute;left:159px;top:172px;width:883px;height:291px;background:var(--frame);border-radius:6px 6px 0 0}
.hero-photo{position:absolute;left:170px;top:181px;width:858px;height:309px;border-radius:4px;
  background:linear-gradient(180deg,#3d6fa6 0%,#7ea3c8 35%,#a9bfd6 60%,#5b7ea4 100%)}
.hero-shadow{position:absolute;left:180px;top:492px;width:838px;height:30px;
  background:radial-gradient(ellipse at 50% 0%,rgba(0,0,0,.55) 0%,rgba(0,0,0,0) 70%)}
.content{position:absolute;left:171px;top:537px;width:857px;height:390px;border:1px solid var(--panel-border);border-radius:8px;
  background:linear-gradient(180deg,#fff 0%,#f4f4f5 45%,#ececee 100%)}
.content h2{position:absolute;left:19px;top:18px;font-size:17px;font-weight:400}
.content .rule{position:absolute;left:21px;top:44px;width:588px;height:1px;background:var(--rule)}
.intro{position:absolute;left:20px;top:60px;width:545px;font-size:11.6px;line-height:19.4px;text-align:justify}
.intro p+p{margin-top:19.4px}
.content h3{position:absolute;left:22px;top:217px;font-size:16px;font-weight:400}
.specialties{position:absolute;left:26px;top:247px;list-style:none}
.specialties li{height:27.7px;font-size:14.4px;display:flex;align-items:center}
.specialties svg{width:9px;height:10px;margin-right:12px}
.photo{position:absolute;left:608px;width:222px;height:147px;border:1px solid #b8b8b8}
.photo-cabin{top:56px;background:linear-gradient(180deg,#e9dfcf 0%,#b89c73 55%,#6e4a2c 100%)}
.photo-jet{top:223px;height:147px;background:linear-gradient(160deg,#2f6a8a 0%,#4c8aa3 45%,#5c6b62 100%)}
.nav{position:absolute;left:442px;top:950px;width:328px;height:31px;border-radius:5px;display:flex;overflow:hidden;
  background:linear-gradient(180deg,#555 0%,#1a1a1a 30%,#000 100%);box-shadow:0 8px 8px -4px rgba(0,0,0,.45)}
.nav a{flex:none;display:flex;align-items:center;justify-content:center;color:#fff;text-decoration:none;font-size:12px;border-right:1px solid #444}
.nav a:nth-child(1){width:101px}
.nav a:nth-child(2){width:110px;color:var(--nav-accent)}
.nav a:nth-child(3){width:117px;border-right:0}
.footer{position:absolute;left:0;top:1003px;width:1200px;height:80px;background:var(--footer);color:var(--footer-text);font-size:12px;text-align:center;padding-top:30px}
</style>
</head>
<body>
<div class="top-bar"></div>

<header class="brand">
  <div class="brand-mark"></div>
  <div class="brand-name">Meridian Crew</div>
</header>

<div class="hero-band"></div>
<div class="hero-frame"></div>
<div class="hero-photo" role="img" aria-label="Business jet in flight above the clouds"></div>
<div class="hero-shadow"></div>

<main class="content">
  <h2>What we do:</h2>
  <div class="rule"></div>
  <div class="intro">
    <p>Meridian Crew Leasing is a service provider to the Business Aviation community, providing qualified pilots for aircraft owners and operators, flying the Veltrane Skyrunner series of aircraft.</p>
    <p>At Meridian Crew Leasing we exclusively focus on the needs of the Business Aviation market and its discerning clients. We demand the best of our crew, who are tasked in providing short/long term crewing. All our crews have multiple years experience in the VVIP market, are highly qualified and come from various backgrounds including Military, Airline and Instruction.</p>
  </div>
  <h3>We specialize in:</h3>
  <ul class="specialties">
    <li><svg viewBox="0 0 9 10"><path d="M1 1l5 4-5 4" fill="none" stroke="#222" stroke-width="2"/></svg>Short notice crewing</li>
    <li><svg viewBox="0 0 9 10"><path d="M1 1l5 4-5 4" fill="none" stroke="#222" stroke-width="2"/></svg>Short term/long term crewing</li>
    <li><svg viewBox="0 0 9 10"><path d="M1 1l5 4-5 4" fill="none" stroke="#222" stroke-width="2"/></svg>Permanent crew placement/hiring support</li>
    <li><svg viewBox="0 0 9 10"><path d="M1 1l5 4-5 4" fill="none" stroke="#222" stroke-width="2"/></svg>Aircraft ferry</li>
    <li><svg viewBox="0 0 9 10"><path d="M1 1l5 4-5 4" fill="none" stroke="#222" stroke-width="2"/></svg>New/pre-owned aircraft delivery</li>
  </ul>
  <div class="photo photo-cabin" role="img" aria-label="Business jet cabin interior with leather seats"></div>
  <div class="photo photo-jet" role="img" aria-label="Business jet flying over mountains"></div>
</main>

<nav class="nav">
  <a href="#">Home</a>
  <a href="#">Services</a>
  <a href="#">Contact Us</a>
</nav>

<footer class="footer">Copyrights @ 2012 All Rights Reserved</footer>
</body>
</html>
```